Weightloss company needs Business Card

We want a business card that is clean and professional, yet portrays that we are a friendly, innovative, and versatile program designed to fit the needs of our clients.
I would like there to be 2 sides, one side having an appointment card, and the other side containing the logo and business information. There can be decorations on both sides. The logo is attached.

Target Market(s)

Men and women 40-60

Industry/Entity Type

Business

Contact Information for Business Card

Font styles to use
Sans Serif

Requirements
Must have
• The logo, space for business information
Nice to have
• The colors in the logo
Should not have
• No pictures of people or food

```html
<!DOCTYPE html>
<html lang="en">
<head>
<meta charset="utf-8">
<title>Ridgeline Weightloss – Business Card</title>
<link href="https://fonts.googleapis.com/css2?family=Arimo:wght@400;700&display=swap" rel="stylesheet">
<style>
  :root {
    --brand-red: #f5002d;
    --ink: #111111;
    --accent-cyan: #27c3ee;
    --bg-light: #ffffff;
    --bg-tint: #eaf8fc;
  }
  * { box-sizing: border-box; margin: 0; padding: 0; }
  html, body {
    width: 1200px;
    height: 600px;
    overflow: hidden;
    background: var(--bg-light);
  }
  .card {
    position: relative;
    width: 1200px;
    height: 600px;
    overflow: hidden;
    background: linear-gradient(135deg, var(--bg-light) 0%, var(--bg-tint) 100%);
    font-family: "Arimo", Arial, sans-serif;
  }
  .card__divider {
    position: absolute;
    inset: 0;
  }
  .brand {
    position: absolute;
    left: 30px;
    top: 262px;
    width: 500px;
    display: flex;
    align-items: center;
    gap: 14px;
  }
  .brand__dot {
    width: 22px;
    height: 22px;
    border-radius: 50%;
    background: var(--brand-red);
    flex: none;
  }
  .brand__name {
    color: var(--brand-red);
    font-weight: 700;
    font-size: 46px;
    line-height: 1.05;
    letter-spacing: 0.5px;
  }
  .identity {
    position: absolute;
    right: 80px;
    top: 72px;
    text-align: right;
  }
  .identity__name {
    color: var(--brand-red);
    font-size: 80px;
    font-weight: 400;
    line-height: 1;
  }
  .identity__title {
    color: var(--ink);
    font-size: 37px;
    line-height: 1.2;
    margin-top: 4px;
  }
  .contact {
    position: absolute;
    right: 80px;
    top: 232px;
    list-style: none;
    text-align: right;
  }
  .contact__item {
    display: flex;
    justify-content: flex-end;
    align-items: center;
    gap: 12px;
    color: var(--brand-red);
    font-size: 25px;
    height: 36px;
  }
  .contact__icon {
    width: 26px;
    height: 26px;
    flex: none;
  }
  .address {
    position: absolute;
    right: 80px;
    top: 368px;
    text-align: right;
    color: var(--brand-red);
    font-size: 25px;
    font-style: normal;
    line-height: 34px;
  }
</style>
</head>
<body>
<main class="card">
  <svg class="card__divider" width="1200" height="600" viewBox="0 0 1200 600" aria-hidden="true">
    <polyline points="680,-10 592,300 680,610" fill="none" stroke="var(--brand-red)" stroke-width="14" stroke-linejoin="miter"/>
  </svg>

  <div class="brand">
    <span class="brand__dot"></span>
    <span class="brand__name">Ridgeline Weightloss</span>
  </div>

  <header class="identity">
    <h1 class="identity__name">Daniel Hart</h1>
    <p class="identity__title">Managing Director</p>
  </header>

  <ul class="contact">
    <li class="contact__item">
      <span>(42) 1630 482 907</span>
      <svg class="contact__icon" viewBox="0 0 26 26" aria-hidden="true">
        <rect x="7" y="3" width="12" height="20" rx="2.5" fill="none" stroke="var(--accent-cyan)" stroke-width="2.4"/>
        <line x1="11" y1="19" x2="15" y2="19" stroke="var(--accent-cyan)" stroke-width="2"/>
      </svg>
    </li>
    <li class="contact__item">
      <span>hello@ridgelinewl.com</span>
      <svg class="contact__icon" viewBox="0 0 26 26" aria-hidden="true">
        <rect x="2" y="5" width="22" height="16" fill="none" stroke="var(--accent-cyan)" stroke-width="2"/>
        <polyline points="2,5 13,14 24,5" fill="none" stroke="var(--accent-cyan)" stroke-width="2"/>
      </svg>
    </li>
    <li class="contact__item">
      <span>www.ridgelinewl.com</span>
      <svg class="contact__icon" viewBox="0 0 26 26" aria-hidden="true">
        <g fill="none" stroke="var(--accent-cyan)" stroke-width="1.4">
          <circle cx="13" cy="13" r="9"/>
          <ellipse cx="13" cy="13" rx="4" ry="9"/>
          <line x1="4" y1="13" x2="22" y2="13"/>
          <line x1="5.5" y1="8.5" x2="20.5" y2="8.5"/>
          <line x1="5.5" y1="17.5" x2="20.5" y2="17.5"/>
        </g>
      </svg>
    </li>
  </ul>

  <address class="address">
    Postal Address number<br>
    CITY/ZIP
  </address>
</main>
</body>
</html>
```